FAIRWAY LEGAL DEFENSE

I'm virtually ready to launch my site, but I have a number of edits and modifications that need to be implemented. More importantly, I'm always looking to improve my site, particularly now that I am making my proverbial "FIRST IMPRESSION." Thus, I'm willing to see if there is someone who can add creativity and perhaps improve what I already have, particularly on the All Important Front Page.

Need extra days to review

```html
<!DOCTYPE html>
<html lang="en">
<head>
<meta charset="utf-8">
<title>Fairway Legal Defense</title>
<link href="https://fonts.googleapis.com/css2?family=Tinos:wght@400;700&family=Open+Sans:wght@400;600;700&display=swap" rel="stylesheet">
<style>
:root{
  --navy:#0d2a5e;
  --deep:#12304a;
  --red:#a80d14;
  --ink:#555b66;
  --light:#f2f2f2;
  --grey:#ececec;
  --field:#f6f6f7;
  --footer:#23232f;
  --white:#ffffff;
}
*{box-sizing:border-box;margin:0;padding:0}
html,body{width:1200px;height:4692px;overflow:hidden;background:var(--white)}
body{position:relative;font-family:"Open Sans",Arial,sans-serif;color:var(--ink)}
.abs{position:absolute}
.serif{font-family:"Tinos","Times New Roman",serif}
.label{position:absolute;font-size:8px;font-weight:700;letter-spacing:.3px;color:var(--navy);text-transform:uppercase}
.title{position:absolute;font-family:"Tinos","Times New Roman",serif;font-weight:700;color:var(--navy);line-height:1.1}
.rule{position:absolute;width:29px;height:2px;background:var(--red)}
.body-text{position:absolute;font-size:13px;line-height:20px;color:var(--ink)}
.btn{position:absolute;width:133px;height:53px;background:var(--red);color:var(--white);font-size:9px;font-weight:700;display:flex;align-items:center;justify-content:center;text-transform:uppercase;letter-spacing:.2px}
.photo{position:absolute}

/* hero */
.hero{position:absolute;left:0;top:0;width:1014px;height:656px;background:var(--light)}
.nav a{position:absolute;top:38px;font-size:13px;color:#666;text-decoration:none}
.brand{position:absolute;left:142px;top:82px;display:flex;align-items:center;gap:10px}
.brand-dot{width:36px;height:36px;border-radius:50%;background:var(--navy)}
.brand-name{font-family:"Tinos",serif;font-weight:700;font-size:14px;color:var(--navy)}

/* services */
.services{position:absolute;left:0;top:1280px;width:1200px;height:729px;background:var(--grey)}
.card{position:absolute;top:266px;width:319px;height:293px;background:var(--white)}
.card .photo{left:0;top:0;width:319px;height:191px}
.card span{position:absolute;left:0;right:0;top:234px;text-align:center;font-family:"Tinos",serif;font-size:21px;color:var(--navy)}

/* video */
.video{position:absolute;left:0;top:2009px;width:1200px;height:453px;background:linear-gradient(135deg,#1b2a3c 0%,#2d3b4c 40%,#17222f 100%)}

/* reasons */
.reason{position:absolute;width:252px;height:158px;background:var(--white);border:1px solid #efefef;box-shadow:0 2px 10px rgba(0,0,0,.05)}
.reason svg{position:absolute;left:30px;top:30px}
.reason b{position:absolute;left:30px;top:88px;font-family:"Tinos",serif;font-weight:400;font-size:18px;line-height:21px;color:var(--navy)}
.reason i{position:absolute;right:26px;top:34px;font-family:"Tinos",serif;font-style:normal;font-size:78px;color:#e3e3e6}

/* feature */
.feature{position:absolute;left:0;top:2968px;width:1200px;height:492px;background:linear-gradient(100deg,#23303f 0%,#354456 55%,#2a3746 100%)}
.quote{position:absolute;left:381px;top:3369px;width:661px;height:270px;background:var(--white);box-shadow:0 4px 24px rgba(0,0,0,.08)}

/* contact */
.field{position:absolute;background:var(--field);font-size:10px;color:#888;padding:22px 20px}

/* footer */
.footer{position:absolute;left:0;top:4301px;width:1200px;height:391px;background:var(--footer)}
.footer .small{position:absolute;font-size:9px;color:#9a9aa8;text-transform:uppercase}
.footer .addr{position:absolute;font-family:"Tinos",serif;font-size:18px;color:var(--white)}
</style>
</head>
<body>

<!-- Hero -->
<section class="hero">
  <nav class="nav">
    <a style="left:340px">HOME</a>
    <a style="left:441px">ABOUT US</a>
    <a style="left:583px">SERVICES</a>
    <a style="left:712px">CONTACT US</a>
  </nav>
  <div class="brand"><div class="brand-dot"></div><div class="brand-name">FAIRWAY LEGAL DEFENSE</div></div>
  <div class="label" style="left:142px;top:182px">About us</div>
  <h1 class="title" style="left:142px;top:206px;font-size:62px;width:560px">Legal Mastery,<br>Client Success</h1>
  <div class="rule" style="left:142px;top:358px"></div>
  <p class="body-text" style="left:142px;top:400px;width:380px;font-size:12.5px;line-height:20px">Lorem ipsum dolor sit amet, consectetur adipiscing elit,<br>sed do eiusmod tempor incididunt ut labore et dolore</p>
  <div class="btn" style="left:142px;top:462px">Learn more</div>
</section>
<div class="photo" role="img" aria-label="Lawyers shaking hands with a client in a bright office" style="left:592px;top:73px;width:574px;height:517px;background:linear-gradient(135deg,#c9c4bc 0%,#a89f94 40%,#4e5563 75%,#262c38 100%)"></div>

<!-- About -->
<div class="photo" role="img" aria-label="Two attorneys in conversation at a meeting" style="left:142px;top:761px;width:366px;height:386px;background:linear-gradient(120deg,#d8d8d6 0%,#8e8f93 45%,#2c3140 100%)"></div>
<div class="abs" style="left:219px;top:1062px;width:364px;height:149px;background:var(--deep)">
  <svg class="abs" style="left:64px;top:60px" width="36" height="36" viewBox="0 0 24 24" fill="none" stroke="#fff" stroke-width="1.4"><path d="M5 3h4l2 5-2.5 1.5a11 11 0 0 0 6 6L16 13l5 2v4a2 2 0 0 1-2 2A17 17 0 0 1 3 5a2 2 0 0 1 2-2z"/></svg>
  <div class="abs serif" style="left:118px;top:48px;font-size:16px;color:#fff">For Calls:</div>
  <div class="abs serif" style="left:118px;top:70px;font-size:26px;font-weight:700;color:#fff">0 800-555-01-47</div>
</div>
<div class="label" style="left:665px;top:766px">About us</div>
<h2 class="title" style="left:665px;top:792px;font-size:52px;width:520px">Strategic Solutions,<br>Legal Excellence</h2>
<div class="rule" style="left:665px;top:924px"></div>
<p class="body-text" style="left:665px;top:950px;width:418px;font-size:12.5px;line-height:20.5px">Lorem ipsum dolor sit amet, consectetur adipiscing elit, sed do eiusmod tempor incididunt ut labore et dolore magna aliqua. Ut enim ad minim veniam, quis nostrud exercitation ullamco laboris nisi ut aliquip ex ea commodo consequat. Duis aute irure dolor in reprehenderit in voluptate velit esse cillum dolore eu fugiat nulla pariatur. Excepteur sint occaecat cupidatat non proident, sunt in culpa qui officia deserunt mollit dolore eu fugiat nulla pariatur. Excepteur sint occaecat</p>
<div class="btn" style="left:665px;top:1145px">Learn more</div>

<!-- Services -->
<section class="services">
  <div class="label" style="left:97px;top:95px">Our services</div>
  <h2 class="title" style="left:97px;top:118px;font-size:52px">Services We Provide</h2>
  <div class="rule" style="left:97px;top:209px"></div>
  <div class="card" style="left:93px"><div class="photo" role="img" aria-label="Attorney consulting with clients" style="background:linear-gradient(120deg,#3b6f93,#c9d3dc 55%,#e8ecef)"></div><span>Consultation</span></div>
  <div class="card" style="left:441px"><div class="photo" role="img" aria-label="Judge's gavel on a courtroom bench" style="background:linear-gradient(120deg,#2a1d14,#7a5232 50%,#c79a66)"></div><span>Litigation</span></div>
  <div class="card" style="left:787px"><div class="photo" role="img" aria-label="Digital legal icons over a hand" style="background:linear-gradient(120deg,#9fb4cc,#3d5e8f 55%,#1c3060)"></div><span>Collection Claims</span></div>
  <div class="btn" style="left:527px;top:603px;height:51px">Learn more</div>
</section>

<!-- Video -->
<section class="video" role="img" aria-label="Dimmed photo of hands passing a document">
  <svg class="abs" style="left:517px;top:120px" width="160" height="160"><circle cx="80" cy="80" r="79" fill="none" stroke="#fff" stroke-width="1.5"/></svg>
  <div class="abs" style="left:517px;top:190px;width:160px;text-align:center;font-size:15px;color:#fff">Play Video</div>
  <div class="abs serif" style="left:0;width:1200px;top:310px;text-align:center;font-size:50px;color:#fff;padding-left:30px">Explanation Video</div>
</section>

<!-- Why choose -->
<div class="label" style="left:107px;top:2569px">About us</div>
<h2 class="title" style="left:107px;top:2592px;font-size:52px;width:320px">Why Choose<br>Us</h2>
<div class="rule" style="left:107px;top:2725px"></div>
<p class="body-text" style="left:107px;top:2748px;width:400px;font-size:12.5px;line-height:20px">Lorem ipsum dolor sit amet, consectetur adipiscing elit, sed do eiusmod tempor incididunt ut labore et dolore magna aliqua. Ut enim ad minim veniam, quis.</p>
<div class="btn" style="left:106px;top:2835px;height:51px">Learn more</div>

<div class="reason" style="left:583px;top:2566px">
  <svg width="38" height="38" viewBox="0 0 24 24" fill="none" stroke="#0d2a5e" stroke-width="1.3"><circle cx="12" cy="13" r="9"/><path d="M12 13l3-4"/><path d="M7 16h10"/></svg>
  <b>Client<br>Centric</b><i>1</i></div>
<div class="reason" style="left:845px;top:2566px">
  <svg width="38" height="38" viewBox="0 0 24 24" fill="none" stroke="#0d2a5e" stroke-width="1.3"><circle cx="12" cy="12" r="9"/><path d="M12 12l4-3"/><path d="M6 14h12"/></svg>
  <b>Free<br>Consultation</b><i>2</i></div>
<div class="reason" style="left:583px;top:2732px">
  <svg width="38" height="38" viewBox="0 0 24 24" fill="none" stroke="#0d2a5e" stroke-width="1.3"><path d="M5 20h14"/><path d="M8 17l6-10 3 2-6 10z"/><path d="M6 14l3 2"/></svg>
  <b>Minimize<br>Exposure</b><i>3</i></div>
<div class="reason" style="left:845px;top:2732px">
  <svg width="38" height="38" viewBox="0 0 24 24" fill="none" stroke="#0d2a5e" stroke-width="1.3"><path d="M12 3l8 6-3 11H7L4 9z"/></svg>
  <b>Affordable<br>Services</b><i>4</i></div>

<!-- Feature -->
<section class="feature" role="img" aria-label="Dimmed photo of a legal team at work">
  <div class="label" style="left:153px;top:95px;color:#fff">About us</div>
  <h2 class="title" style="left:153px;top:107px;font-size:60px;color:#fff;width:800px">Resolute Legal Solutions,<br>Tailored for You</h2>
  <p class="body-text" style="left:153px;top:279px;width:420px;color:#fff;font-size:12.5px">Lorem ipsum dolor sit amet, consectetur adipiscing elit,<br>sed do eiusmod tempor incididunt ut labore et dolore magna</p>
  <div class="btn" style="left:155px;top:341px;height:51px">Learn more</div>
</section>
<div class="quote">
  <p class="abs serif" style="left:78px;top:58px;width:412px;font-size:17px;line-height:25.5px;color:#666">Lorem ipsum dolor sit amet, consectetur adi sed do eiusmod tempor incididunt ut labore ent aliqua. Ut enim ad minim veniam, quis nostru ullamco laboris nisi ut aliquip ex ea commodo aute irure dolor in reprehenderit in voluptate v dolore eu fugiat nulla pariatur. Excepteur sint occ</p>
  <svg class="abs" style="left:530px;top:100px" width="74" height="56" viewBox="0 0 74 56" fill="#0d2a5e"><path d="M0 0h30v30l-10 26H6l8-24H0z"/><path d="M40 0h30v30l-10 26H46l8-24H40z"/></svg>
</div>

<!-- Contact -->
<div class="photo" role="img" aria-label="Two lawyers standing back to back" style="left:151px;top:3720px;width:361px;height:424px;background:linear-gradient(160deg,#cfd8dc 0%,#9ba8ae 50%,#3a4250 100%)"></div>
<div class="abs" style="left:239px;top:4039px;width:273px;height:105px;background:var(--deep)">
  <div class="abs" style="left:0;right:0;top:36px;text-align:center;font-size:8px;font-weight:700;color:#fff">NEED TO CONTACT US?</div>
  <div class="abs serif" style="left:0;right:0;top:52px;text-align:center;font-size:19px;color:#fff">Email Us</div>
</div>
<div class="label" style="left:610px;top:3691px">Contact us</div>
<h2 class="title" style="left:610px;top:3718px;font-size:52px;width:420px">Get in touch with<br>us</h2>
<div class="rule" style="left:610px;top:3849px"></div>
<div class="field" style="left:606px;top:3897px;width:215px;height:55px">My name is:</div>
<div class="field" style="left:825px;top:3897px;width:217px;height:55px">My e-mail:</div>
<div class="field" style="left:606px;top:3955px;width:436px;height:53px">I am interested in:</div>
<div class="field" style="left:606px;top:4012px;width:436px;height:135px">My message is:</div>
<div class="btn" style="left:903px;top:4161px">Learn more</div>

<!-- Footer -->
<footer class="footer">
  <div class="small" style="left:104px;top:101px">Visit office:</div>
  <div class="addr" style="left:104px;top:121px">45 Harbor Rd. Suite, 210</div>
  <div class="small" style="left:104px;top:176px">Visit office:</div>
  <div class="addr" style="left:104px;top:196px">45 Harbor Rd. Suite, 210</div>
  <div class="small" style="left:104px;top:251px">Visit office:</div>
  <div class="addr" style="left:104px;top:271px">45 Harbor Rd. Suite, 210</div>

  <svg class="abs" style="left:504px;top:90px" width="140" height="140"><circle cx="70" cy="70" r="68" fill="#1e3a72"/></svg>
  <div class="abs serif" style="left:400px;width:348px;top:274px;text-align:center;font-size:14px;font-weight:700;color:#fff">FAIRWAY LEGAL DEFENSE</div>

  <div class="small" style="left:869px;top:128px">Subscribe to our news</div>
  <div class="abs serif" style="left:869px;top:148px;font-size:17px;line-height:20px;color:#fff">Always Get Our Latest News<br>&amp; Events Newsletter</div>
  <div class="abs" style="left:869px;top:228px;width:178px;height:38px;background:#3a3a48;font-size:11px;color:#9a9aa8;padding:11px 18px">your email</div>
  <div class="abs" style="left:1053px;top:228px;width:49px;height:38px;background:var(--red)">
    <svg class="abs" style="left:15px;top:9px" width="20" height="20" viewBox="0 0 20 20" fill="none" stroke="#fff" stroke-width="2.6"><path d="M7 3l7 7-7 7"/></svg>
  </div>
</footer>

</body>
</html>
```